Flyer-Design für Immobilienmarketing von Raumfreude Home Staging
Zielgruppe
Wir (Raumfreude Home Staging) geben mit Home Staging Immobilien ein Raumfreude (www.raumfreude-beispiel.de). Ziel ist die Immobilienvermarktung zu beschleunigen (Immobilienmarketing) und den besten Preis zu erzielen. Durch ein eigenes Möbel und Dekolager erfolgt die Gestaltung zeitnah.
Zielgruppe sind Immobilienverkäufer (privat) und auch Makler/Vermittler/Projektentwickler
Aufgabenstellung
Wir benötigen einen Flyer/Klappkarte DIN lang quer. Dieser sollte hochwertig, einladend, hell und freundlich erscheinen. Wenn er an der langen Seite gefaltet ist, sollte er als Klappkarte auf dem Tisch stehen können. Dabei sollen alle 4 Seiten genutzt werden. Logo und Design sowie Kurzbeschreibungen/Texte entsprechend bitte der Website (www.raumfreude-beispiel.de) verwenden. Originale können zur Verfügung gestellt werden. Der Flyer sollte auch als PDF nutzbar sein.
Als Slogan stellen wir uns folgendes vor 'Mit Raumfreude in den Immobilienverkauf starten und beim besten Preis landen', sind aber für alles offen. Bei Verwendung von Referenzen wäre ein Spruch mit 'Wohlfühlen' gut. Des Weiteren einfach bei den Texten und Bildern der Website bedienen (Vorteile + warum mit uns) und einen knackigen überzeugenden Flyer bei dem hauptsächlich die Bilder sprechen, erstellen. Wir freuen uns auf die Vorschläge.

```html
<!DOCTYPE html>
<html lang="de">
<head>
<meta charset="utf-8">
<title>Raumfreude Home Staging – Klappkarte</title>
<link rel="stylesheet" href="https://fonts.googleapis.com/css2?family=Open+Sans:wght@300;400;600;700&display=swap">
<style>
  :root {
    --stage: #e2ecc2;
    --paper: #ffffff;
    --paper-soft: #f4f4f3;
    --ink: #3b3b3b;
    --ink-soft: #666666;
    --green: #8cb43a;
    --green-light: #a6c95a;
    --photo-light: #ecebe7;
    --photo-mid: #c9c5bd;
    --photo-wood: #b69a7a;
    --photo-green: #5f8a6a;
  }
  * { box-sizing: border-box; margin: 0; padding: 0; }
  html, body { width: 816px; height: 1200px; overflow: hidden; }
  body {
    background: var(--stage);
    font-family: "Open Sans", Arial, sans-serif;
    color: var(--ink);
    display: flex;
    flex-direction: column;
    align-items: center;
    justify-content: space-evenly;
  }
  .spread {
    width: 640px;
    height: 560px;
    display: flex;
    flex-direction: column;
    box-shadow: 0 10px 28px rgba(80, 110, 30, 0.18);
  }
  .panel {
    position: relative;
    width: 640px;
    height: 280px;
    background: var(--paper);
    overflow: hidden;
  }
  .panel + .panel { border-top: 1px solid #e6e6e6; }
  .panel svg.photo-layer { position: absolute; inset: 0; }

  /* Cover */
  .cover-text { position: absolute; left: 44px; top: 40px; width: 330px; }
  .brand-name {
    display: flex; align-items: center; gap: 10px;
    font-weight: 300; font-size: 27px; color: var(--ink); letter-spacing: 0.3px;
  }
  .brand-dot { width: 12px; height: 12px; border-radius: 50%; background: var(--green); flex: none; }
  .brand-rule { width: 230px; height: 2px; background: var(--green); margin: 18px 0 16px; }
  .slogan { font-weight: 300; font-size: 15px; line-height: 1.5; color: var(--ink-soft); }
  .website { margin-top: 16px; font-size: 12px; color: var(--ink-soft); letter-spacing: 0.4px; }

  /* Benefits */
  .benefit-list {
    position: absolute; left: 270px; top: 52px;
    list-style: none;
  }
  .benefit-list li {
    display: flex; align-items: center; gap: 14px;
    font-size: 18px; font-weight: 400; color: var(--ink);
    margin-bottom: 22px;
  }
  .tick { width: 18px; height: 14px; flex: none; }

  /* Inside photo panel */
  .claim-pill {
    position: absolute; left: 40px; bottom: 34px;
    background: var(--green); color: #fff;
    border-radius: 28px;
    padding: 16px 34px;
    font-size: 19px; font-weight: 600; line-height: 1.3;
  }

  /* Features */
  .features {
    position: absolute; inset: 0;
    display: flex; gap: 36px;
    padding: 58px 44px 0;
  }
  .feature { flex: 1; display: flex; flex-direction: column; gap: 14px; }
  .feature-icon { width: 52px; height: 52px; }
  .feature-title { font-size: 15px; font-weight: 700; color: var(--ink); }
  .feature-text { font-size: 12.5px; line-height: 1.55; color: var(--ink-soft); }
</style>
</head>
<body>

  <!-- Outside of the folded card -->
  <section class="spread spread--outside">
    <div class="panel panel--cover">
      <svg class="photo-layer" width="640" height="280" viewBox="0 0 640 280">
        <defs>
          <linearGradient id="coverPhoto" x1="0" y1="0" x2="1" y2="1">
            <stop offset="0" stop-color="var(--photo-light)"/>
            <stop offset="0.55" stop-color="var(--photo-mid)"/>
            <stop offset="0.8" stop-color="var(--photo-green)" stop-opacity="0.55"/>
            <stop offset="1" stop-color="var(--photo-wood)"/>
          </linearGradient>
        </defs>
        <polygon points="330,280 640,90 640,280" fill="url(#coverPhoto)"
          role="img" aria-label="Foto: gestaltetes Wohnzimmer mit grünem Sessel, Bogenleuchte und großen Fenstern"/>
      </svg>
      <div class="cover-text">
        <div class="brand-name"><span class="brand-dot"></span>Raumfreude Home Staging</div>
        <div class="brand-rule"></div>
        <p class="slogan">Mit Raumfreude in den<br>Immobilienverkauf starten<br>&amp; beim besten Preis landen</p>
        <p class="website">www.raumfreude-beispiel.de</p>
      </div>
    </div>

    <div class="panel panel--benefits" style="background: var(--paper-soft);">
      <svg class="photo-layer" width="640" height="280" viewBox="0 0 640 280">
        <defs>
          <linearGradient id="benefitPhoto" x1="0" y1="0" x2="1" y2="1">
            <stop offset="0" stop-color="var(--photo-light)"/>
            <stop offset="0.5" stop-color="var(--photo-mid)"/>
            <stop offset="1" stop-color="var(--photo-wood)"/>
          </linearGradient>
        </defs>
        <polygon points="0,0 250,0 160,280 0,280" fill="url(#benefitPhoto)"
          role="img" aria-label="Foto: helles Zimmer mit Sprossenfenstern, Glastisch und grüner Decke"/>
      </svg>
      <ul class="benefit-list">
        <li><svg class="tick" viewBox="0 0 18 14"><polygon points="0,0 18,0 10,14" fill="var(--green)"/></svg>das größte Interesse wecken</li>
        <li><svg class="tick" viewBox="0 0 18 14"><polygon points="0,0 18,0 10,14" fill="var(--green)"/></svg>viel Zeit und Nerven sparen</li>
        <li><svg class="tick" viewBox="0 0 18 14"><polygon points="0,0 18,0 10,14" fill="var(--green)"/></svg>den besten Preis erzielen</li>
        <li><svg class="tick" viewBox="0 0 18 14"><polygon points="0,0 18,0 10,14" fill="var(--green)"/></svg>schnell Käufer finden</li>
      </ul>
    </div>
  </section>

  <!-- Inside of the folded card -->
  <section class="spread spread--inside">
    <div class="panel panel--photo">
      <svg class="photo-layer" width="640" height="280" viewBox="0 0 640 280">
        <defs>
          <linearGradient id="insidePhoto" x1="0" y1="0" x2="1" y2="1">
            <stop offset="0" stop-color="var(--photo-light)"/>
            <stop offset="0.45" stop-color="#d9d7d1"/>
            <stop offset="0.75" stop-color="var(--photo-mid)"/>
            <stop offset="1" stop-color="#9a8f84"/>
          </linearGradient>
        </defs>
        <rect width="640" height="280" fill="url(#insidePhoto)"
          role="img" aria-label="Foto: offener Wohn- und Essbereich mit Holztisch, hellen Stühlen, Kamin und Fensterfront"/>
      </svg>
      <div class="claim-pill">Wir geben Räumen<br>ein Gesicht zum Wohlfühlen</div>
    </div>

    <div class="panel panel--features">
      <div class="features">
        <div class="feature">
          <svg class="feature-icon" viewBox="0 0 52 52">
            <rect x="22" y="3" width="8" height="5" rx="1" fill="var(--green)"/>
            <circle cx="26" cy="29" r="19" fill="none" stroke="var(--green)" stroke-width="4"/>
            <path d="M26 29 L26 16 A13 13 0 1 1 13 29 Z" fill="var(--green)"/>
          </svg>
          <h3 class="feature-title">Schnelle &amp; individuelle Einrichtung</h3>
          <p class="feature-text">Mit unserem eigenen Möbellager garantieren Wir Ihnen eine schnelle und individuelle Einrichtung Ihrer Immobilie</p>
        </div>
        <div class="feature">
          <svg class="feature-icon" viewBox="0 0 52 52">
            <rect x="6" y="22" width="9" height="24" rx="1.5" fill="var(--green)"/>
            <path d="M18 24 L27 8 C30 6 33 8 32 12 L30 20 L42 20 C46 20 47 24 45 27 L41 42 C40 45 38 46 35 46 L18 46 Z" fill="var(--green)"/>
          </svg>
          <h3 class="feature-title">Wir wissen was gut ankommt!</h3>
          <p class="feature-text">Unsere gesammelten Erfahrungen setzen wir gezielt ein, damit sich jede Immobilie schnell und zum besten Preis verkauft.</p>
        </div>
      </div>
    </div>
  </section>

</body>
</html>
```